Zellmoor Ridged Concrete & Grinding
I'm looking for a business card and logo design for my
new Polished Concrete & Grinding business,
If you were to look up Zellmoor in the dictionary it would
say, first in importance, order, or position; leading.
Polished Concrete floors are a niche market, that are being used currently in Shopping centres, office spaces and by most high end architects, builders and designers.
i need my business card & logo to stand out from my
competitors, i need my design + logo to reflect this it
needs to be simple, professional, eye catching, easy
to read and scream quality. The logo will need to be
suitable for a whole range of applications including,
uniforms, letter heads, stickers, and eventually
incorporating in vehicle vinyl wrapping.
Target Market(s)
Builders, architects, Interior designers & home owners
Contact Information for Business Card
Front side:
- Vantor Ridged Concrete & Grinding.
- Logo
Rear side:
- Neil Varbusk
- 0491587302
- info@zellmoorrcg.example
- commercial - domestic - industrial
- (later down the line website & space for
social media links
www.zellmoorridgedconcrete.example)
Colors
Designer to choose colors to be used in the design.
Look and feel

```html
<!DOCTYPE html>
<html lang="en">
<head>
<meta charset="utf-8">
<title>Zellmoor Ridged Concrete &amp; Grinding – Business Card</title>
<link href="https://fonts.googleapis.com/css2?family=Montserrat:wght@800&family=Exo+2:wght@700&family=Roboto:wght@400;500&display=swap" rel="stylesheet">
<style>
  :root {
    --stage: #e9e7e3;
    --card-white: #ffffff;
    --band-black: #050505;
    --mark-light: #c9cbcd;
    --mark-grey: #8a8d90;
    --ink: #4a4c4f;
    --ink-name: #55575a;
    --rule-blue: #4e86b9;
    --rule-blue-light: #b3c6da;
    --icon-blue: #4e7fb2;
    --social-a: #3b5998;
    --social-b: #d6376f;
    --social-c: #1d87c4;
    --deco-grey: #e4e4e4;
  }
  * { box-sizing: border-box; margin: 0; padding: 0; }
  html, body { width: 900px; height: 1200px; overflow: hidden; }
  body { background: var(--stage); position: relative; font-family: "Roboto", sans-serif; }

  .card {
    position: absolute; left: 82px; width: 740px; height: 432px;
    border-radius: 44px 0 44px 0; overflow: hidden;
    box-shadow: 0 6px 14px rgba(0,0,0,0.25);
  }
  .card--front { top: 127px; background: var(--band-black); }
  .card--back { top: 634px; background: var(--card-white); }

  .photo-top {
    position: absolute; left: 0; top: 0; width: 100%; height: 143px;
    background: radial-gradient(ellipse at 52% 60%, #c9d0cb 0%, #8d9893 30%, #5e6a65 70%, #4c5753 100%);
  }
  .photo-bottom {
    position: absolute; left: 0; bottom: 0; width: 100%; height: 144px;
    background: linear-gradient(100deg, #b9b4a2 0%, #a19c88 35%, #8f8b78 70%, #7c7866 100%);
  }

  .brand { position: absolute; display: flex; align-items: center; }
  .brand__badge { border-radius: 50%; border: 4px solid currentColor; flex: none; }
  .brand__divider { width: 2px; align-self: stretch; background: currentColor; opacity: 0.6; }
  .brand__name {
    font-family: "Montserrat", sans-serif; font-weight: 800; text-transform: uppercase;
    line-height: 1; white-space: nowrap;
  }
  .brand__name .word { display: block; letter-spacing: 0.5px; }
  .brand__name .line { display: block; letter-spacing: 0.4px; }

  .card--front .brand { left: 138px; top: 162px; height: 106px; color: var(--mark-light); gap: 14px; }
  .card--front .brand__badge { width: 106px; height: 106px; }
  .card--front .brand__name .word { font-size: 52px; }
  .card--front .brand__name .line { font-size: 18px; margin-top: 8px; }

  .card--back .brand { left: 46px; top: 52px; height: 92px; color: var(--mark-grey); gap: 12px; }
  .card--back .brand__badge { width: 92px; height: 92px; }
  .card--back .brand__name .word { font-size: 46px; }
  .card--back .brand__name .line { font-size: 15.5px; margin-top: 7px; }

  .deco-ring {
    position: absolute; left: 428px; top: -60px; width: 340px; height: 340px;
    border-radius: 50%; border: 12px solid var(--deco-grey);
  }

  .contact { position: absolute; left: 44px; top: 226px; color: var(--ink); }
  .contact__name {
    font-family: "Exo 2", sans-serif; font-weight: 700; font-size: 23px;
    letter-spacing: 1.5px; color: var(--ink-name); text-transform: uppercase; margin-bottom: 4px;
  }
  .contact__row { display: flex; align-items: center; gap: 10px; font-size: 17px; height: 29px; }
  .contact__row svg { width: 19px; height: 19px; flex: none; fill: var(--icon-blue); }

  .services {
    position: absolute; left: 8px; top: 370px; width: 572px; height: 30px;
    background: linear-gradient(90deg, var(--rule-blue) 0%, #7b9fc6 60%, var(--rule-blue-light) 100%);
    color: #fff; font-weight: 500; font-size: 17px; letter-spacing: 0.8px;
    padding-left: 36px; line-height: 30px; text-transform: uppercase;
  }
  .social { position: absolute; left: 586px; top: 370px; display: flex; gap: 5px; }
  .social span { width: 32px; height: 32px; display: block; }
  .social .s1 { background: var(--social-a); }
  .social .s2 { background: var(--social-b); }
  .social .s3 { background: var(--social-c); }
</style>
</head>
<body>

<section class="card card--front">
  <div class="photo-top" role="img" aria-label="Photo of a glossy polished grey concrete floor with light reflection"></div>
  <div class="brand">
    <span class="brand__badge"></span>
    <span class="brand__divider"></span>
    <span class="brand__name">
      <span class="word">Zellmoor</span>
      <span class="line">Ridged Concrete &amp; Grinding</span>
    </span>
  </div>
  <div class="photo-bottom" role="img" aria-label="Close-up photo of polished concrete with exposed stone aggregate"></div>
</section>

<section class="card card--back">
  <div class="deco-ring"></div>
  <div class="brand">
    <span class="brand__badge"></span>
    <span class="brand__divider"></span>
    <span class="brand__name">
      <span class="word">Zellmoor</span>
      <span class="line">Ridged Concrete &amp; Grinding</span>
    </span>
  </div>

  <div class="contact">
    <p class="contact__name">Neil Varbusk</p>
    <p class="contact__row">
      <svg viewBox="0 0 24 24"><path d="M6.6 10.8a15.1 15.1 0 0 0 6.6 6.6l2.2-2.2c.3-.3.7-.4 1-.2 1.1.4 2.3.6 3.6.6.6 0 1 .4 1 1V20c0 .6-.4 1-1 1A17 17 0 0 1 3 4c0-.6.4-1 1-1h3.5c.6 0 1 .4 1 1 0 1.3.2 2.5.6 3.6.1.3 0 .7-.2 1z"/></svg>
      0491 587 302
    </p>
    <p class="contact__row">
      <svg viewBox="0 0 24 24"><path d="M2 5h20v14H2z M3.5 6.5 12 13l8.5-6.5v-.1H3.5z" fill-rule="evenodd"/></svg>
      info@zellmoorrcg.example
    </p>
    <p class="contact__row">
      <svg viewBox="0 0 24 24"><path d="M12 2a10 10 0 1 0 0 20 10 10 0 0 0 0-20zm6.9 6h-3a15.6 15.6 0 0 0-1.3-3.9A8 8 0 0 1 18.9 8zM12 4c.8 1.2 1.5 2.5 1.9 4h-3.8c.4-1.5 1.1-2.8 1.9-4zM4.3 14a8 8 0 0 1 0-4h3.4a16 16 0 0 0 0 4zm.8 2h3a15.6 15.6 0 0 0 1.3 3.9A8 8 0 0 1 5.1 16zm3-8h-3a8 8 0 0 1 4.3-3.9C8.8 5.3 8.4 6.6 8.1 8zM12 20c-.8-1.2-1.5-2.5-1.9-4h3.8c-.4 1.5-1.1 2.8-1.9 4zm2.3-6H9.7a14.6 14.6 0 0 1 0-4h4.6a14.6 14.6 0 0 1 0 4zm.3 5.9c.6-1.2 1-2.5 1.3-3.9h3a8 8 0 0 1-4.3 3.9zm1.7-5.9a16 16 0 0 0 0-4h3.4a8 8 0 0 1 0 4z"/></svg>
      www.zellmoorridgedconcrete.example
    </p>
  </div>

  <p class="services">Commercial - Domestic - Industrial</p>
  <div class="social">
    <span class="s1"></span>
    <span class="s2"></span>
    <span class="s3"></span>
  </div>
</section>

</body>
</html>
```